Business cards / Letterheads / Compliment slips

We are looking to get business cards, letterheads and compliment slips designed.

These will all have to follow the design of our new website and logo. Links to the website, logo and fonts can be found below...

The designs need to be simple with focus on the typography. Only the following colours should be used on the designs...

#7f9d3c
#191818
#fff

Website:
http://brightfieldweb.samplework.co.uk/

Logo:
https://www.filecrate.example/sh/9xk2mwq7tvbalp4/qrtuPL8NzK/logos

Fonts:
https://www.filecrate.example/sh/9xk2mwq7tvbalp4/Hw7ZpRt3sQ/Fonts/BayerModern_TTF

and

https://www.filecrate.example/sh/9xk2mwq7tvbalp4/T6nVyo4Dc1/Fonts/MuseoSansFamily

Reason: We would like some more design submissions

Reason: We are still deciding on designs we like and would like to see some more submissions...

Industry/Entity Type

Business

Requirements
Must have
• The designs need to be simple with focus on the typography. Only the following colours should be used on the designs...

#7f9d3c
#191818
#fff
Should not have
• - Any fonts that are not provided.
- Any colours that are not provided.

```html
<!DOCTYPE html>
<html lang="en">
<head>
<meta charset="utf-8">
<title>Brightfieldweb business card</title>
<link rel="stylesheet" href="https://fonts.googleapis.com/css2?family=Mulish:wght@300;400;800&display=swap">
<style>
  :root {
    --green: #7f9d3c;
    --ink: #191818;
    --white: #ffffff;
    --charcoal: #3c3c3c;
    --body-grey: #3a3a3a;
    --backdrop: #d9dcdd;
  }
  html, body {
    margin: 0;
    width: 1200px;
    height: 960px;
    overflow: hidden;
    background: var(--backdrop);
    font-family: "Mulish", Arial, sans-serif;
  }
  .sheet {
    position: relative;
    width: 1200px;
    height: 960px;
  }
  .card {
    position: absolute;
    left: 240px;
    width: 720px;
    height: 400px;
    overflow: hidden;
    box-shadow: 0 10px 28px rgba(0,0,0,0.18);
  }
  .card--front { top: 50px; background: var(--white); }
  .card--back { top: 510px; background: var(--charcoal); }

  .call-band {
    position: absolute;
    left: 0;
    top: 86px;
    width: 360px;
    height: 58px;
    background: var(--green);
    color: var(--white);
    font-size: 26px;
    font-weight: 400;
    line-height: 58px;
    padding-left: 32px;
    box-sizing: border-box;
  }
  .contact {
    position: absolute;
    left: 32px;
    top: 168px;
    color: var(--body-grey);
    font-size: 19px;
    font-weight: 400;
    line-height: 1.35;
  }
  .contact p { margin: 0 0 14px; }
  .holder {
    position: absolute;
    left: 430px;
    top: 62px;
  }
  .holder__name {
    margin: 0;
    color: var(--green);
    font-size: 29px;
    font-weight: 300;
    letter-spacing: 0.02em;
  }
  .holder__role {
    margin: 8px 0 0;
    color: var(--body-grey);
    font-size: 19px;
  }
  .wordmark {
    position: absolute;
    right: 30px;
    bottom: 64px;
    display: flex;
    align-items: center;
    gap: 10px;
  }
  .wordmark__dot {
    width: 38px;
    height: 38px;
    border-radius: 50%;
    background: var(--green);
  }
  .wordmark__name {
    color: var(--charcoal);
    font-size: 34px;
    font-weight: 800;
    letter-spacing: -0.01em;
  }

  .back-circle {
    position: absolute;
    left: -150px;
    top: -60px;
    width: 360px;
    height: 360px;
    border-radius: 50%;
    background: var(--green);
  }
  .back-url {
    position: absolute;
    right: 40px;
    top: 150px;
    color: var(--green);
    font-size: 22px;
    font-weight: 300;
    letter-spacing: 0.05em;
  }
</style>
</head>
<body>
<main class="sheet">
  <section class="card card--front" aria-label="Business card front">
    <div class="call-band">Call: 0854 310 4592</div>
    <div class="contact">
      <p>hello@brightfieldweb.co.uk</p>
      <p>brightfieldweb.samplework.co.uk</p>
      <p>Floor 2, 14 Weaver Lane,<br>Chester , CH2 4LP</p>
    </div>
    <div class="holder">
      <h1 class="holder__name">HELENA MARSH</h1>
      <p class="holder__role">Manager</p>
    </div>
    <div class="wordmark">
      <span class="wordmark__dot"></span>
      <span class="wordmark__name">brightfieldweb</span>
    </div>
  </section>

  <section class="card card--back" aria-label="Business card back">
    <div class="back-circle"></div>
    <div class="back-url">brightfieldweb.samplework.co.uk</div>
  </section>
</main>
</body>
</html>
```